postcard for Real Estate Agent that sells homes for less than any other agents

My company sells houses for a fraction of what others charge. I have most of the verbiage but I am open to ideas.
Our post card will be 6.25 x 9
We need an image that goes with our words and draws people to take a look
We are playful at the same time very serious about the money we will save our clients. In the past our message has been received as too good to be true. Our old message was "save $6000* when you list with us" We think the "*" was causing people to think their was a catch. Other agents will tell people that we will not do what they will do and that is why they must charge more. We are a full service agency and we will generally do everything that other agents will do and in many cases we will do more than other agents. We are changing this industry and need our message to get to every person that is thinking of selling their home

Target Market(s)

People who want to list their home for sale

Industry/Entity Type

Real Estate Agent

Requirements
Must have
• Image that makes people read the message

```html
<!DOCTYPE html>
<html lang="en">
<head>
<meta charset="utf-8">
<title>Keystone Realty – Listing Postcard</title>
<link rel="stylesheet" href="https://fonts.googleapis.com/css2?family=Archivo+Black&family=Arimo:wght@400;700&display=swap">
<style>
  :root {
    --green: #4b9a3a;
    --green-deep: #3f8a31;
    --green-light: #c9e6a3;
    --grass: #78ad45;
    --grass-dark: #5d8f33;
    --wall: #d9d3c9;
    --brick: #a9482f;
    --white: #ffffff;
    --shadow: #1d2a14;
    --navy: #1f3f7a;
    --grey: #555a5e;
    --divider: #9a9a9a;
  }
  * { margin: 0; padding: 0; box-sizing: border-box; }
  html, body { width: 1200px; height: 800px; overflow: hidden; background: var(--white); }
  .postcard {
    position: relative;
    width: 1200px;
    height: 800px;
    font-family: "Arimo", Arial, sans-serif;
  }
  .hero {
    position: absolute;
    inset: 0 0 200px 0;
    background: var(--green);
    overflow: hidden;
  }
  .hero-photo {
    position: absolute;
    top: 0; right: 0;
    width: 780px; height: 600px;
    background:
      radial-gradient(ellipse 220px 90px at 340px 300px, rgba(110,130,90,0.55), transparent 70%),
      linear-gradient(180deg, var(--wall) 0%, #cfc6b8 22%, var(--brick) 24%, #b9866c 38%, #7f9f5a 48%, var(--grass) 60%, var(--grass-dark) 100%);
  }
  .hero-fade {
    position: absolute;
    top: 0; left: 400px;
    width: 260px; height: 600px;
    background: linear-gradient(90deg, var(--green) 0%, rgba(75,154,58,0.8) 45%, rgba(75,154,58,0) 100%);
  }
  .headline {
    position: absolute;
    left: 55px; top: 74px;
    color: var(--white);
    font-weight: 700;
    text-shadow: 3px 3px 0 var(--shadow);
    line-height: 1;
  }
  .headline .lead { font-size: 39px; display: block; }
  .headline .shout {
    font-family: "Archivo Black", "Arial Black", sans-serif;
    font-size: 67px;
    display: block;
    margin: 4px 0 6px;
    letter-spacing: 0.5px;
  }
  .headline .line { font-size: 37px; display: block; margin-top: 6px; }
  .uses-title {
    position: absolute;
    left: 62px; top: 343px;
    color: var(--green-light);
    font-family: "Archivo Black", "Arial Black", sans-serif;
    font-size: 29px;
    line-height: 37px;
    letter-spacing: 0.4px;
  }
  .uses-list {
    position: absolute;
    left: 64px; top: 424px;
    display: grid;
    grid-template-columns: 222px 200px;
    row-gap: 3px;
    list-style: none;
    color: var(--white);
    font-size: 17px;
    font-weight: 700;
  }
  .uses-list li { display: flex; align-items: center; height: 23px; }
  .uses-list li::before {
    content: "";
    width: 0; height: 0;
    border-left: 8px solid var(--green-light);
    border-top: 5px solid transparent;
    border-bottom: 5px solid transparent;
    margin-right: 10px;
  }
  .footer {
    position: absolute;
    left: 0; top: 600px;
    width: 1200px; height: 200px;
    background: var(--white);
  }
  .brand {
    position: absolute;
    left: 78px; top: 82px;
    display: flex;
    align-items: center;
    gap: 12px;
    color: var(--navy);
    font-weight: 700;
    font-size: 32px;
  }
  .brand-mark { width: 26px; height: 26px; background: var(--green); }
  .divider {
    position: absolute;
    left: 412px; top: 35px;
    width: 1px; height: 140px;
    background: var(--divider);
  }
  .contact {
    position: absolute;
    left: 413px; right: 0; top: 40px;
    text-align: center;
  }
  .contact .tagline {
    color: var(--navy);
    font-weight: 700;
    font-size: 22.5px;
    letter-spacing: 0.2px;
  }
  .contact .call {
    color: var(--grey);
    font-size: 35px;
    margin-top: 14px;
  }
  .contact .call strong { font-weight: 700; }
  .contact .web {
    color: var(--navy);
    font-weight: 700;
    font-size: 34px;
    margin-top: 10px;
  }
</style>
</head>
<body>
<main class="postcard">
  <section class="hero">
    <div class="hero-photo" role="img" aria-label="Photo of a frustrated man in a suit sitting on a leaf-strewn front lawn, holding his head, beside a red For Sale sign in front of a brick house"></div>
    <div class="hero-fade"></div>

    <h1 class="headline">
      <span class="lead">You’d have to be</span>
      <span class="shout">Bat $#@T CRAZY</span>
      <span class="line">to give an agent $6000.00</span>
      <span class="line">To put a sign in your yard.</span>
    </h1>

    <h2 class="uses-title">Look at what you<br>can do with $6000.00</h2>
    <ul class="uses-list">
      <li>Give it to your Kids</li>
      <li>Build a fence</li>
      <li>Build a deck</li>
      <li>Buy new clothes</li>
      <li>Landscape</li>
      <li>Take a Vacation</li>
      <li>Pay off your car</li>
      <li>Pay off student loan</li>
      <li>Buy New Carpet</li>
      <li>Upgrade Appliances</li>
    </ul>
  </section>

  <footer class="footer">
    <div class="brand"><span class="brand-mark"></span>Keystone Realty</div>
    <div class="divider"></div>
    <div class="contact">
      <p class="tagline">FULL SERVICE AGENCY AT A FRACTION OF THE COST</p>
      <p class="call">Call Dale or Marcus at <strong>970.555.0142</strong></p>
      <p class="web">www.DaleKeyHomes.com</p>
    </div>
  </footer>
</main>
</body>
</html>
```